LINGERIE WEBSHOP - Velora casa

We are looking for design and layout design for our webshop. We are company that sells lingerie and other connected textile products liki payamas and etc..
Our website will have approx 500 different products within 2 main catogories Woman/Man) and approx. 10 subcategories
Here is what we expect form design:
-Color pallete should be black and white (if you wish you can add some accent color)
-we want to leave feeling to customers of good quality products towards to luxury
-UX should be simple. Feel free to suggest layout
-frontpage layout, product list layout, product description layout, blog layout
-responsive design, compatible with smartphone

Target Market(s)

woman buying for themself, man buying for woman

Industry/Entity Type

Lingerie

Logo Text

VELORA CASA

Number of Pages Required

4 page

Font styles to use
Sans Serif
Decorative

Requirements
Must have
• simple UX
Nice to have
• difference for sexy/luxury lingerie and daily/cozy lingerie
Should not have
• cheap feel, unreliable

```html
<!DOCTYPE html>
<html lang="en">
<head>
<meta charset="utf-8">
<title>Velora Casa – Luxury Lingeries</title>
<link href="https://fonts.googleapis.com/css2?family=Poppins:wght@300;400;500;600&family=Playfair+Display:wght@700&display=swap" rel="stylesheet">
<style>
:root{
  --ink:#1f1f1f;
  --dark:#333333;
  --muted:#8a8a8a;
  --soft:#a9a9a9;
  --line:#e6e6e6;
  --band:#f5f5f5;
  --photo:#f2f2f2;
  --white:#ffffff;
}
*{margin:0;padding:0;box-sizing:border-box}
html,body{width:1200px;height:2172px;overflow:hidden;background:var(--white)}
body{position:relative;font-family:'Poppins',sans-serif;color:var(--ink)}
.abs{position:absolute}
.site-header{left:0;top:0;width:1200px;height:71px;background:var(--dark)}
.logo{font-family:'Poppins',sans-serif;font-weight:300;font-size:17px;letter-spacing:1px;color:var(--white);white-space:nowrap}
.search{left:458px;top:19px;width:314px;height:33px;border-radius:17px;background:#5a5a5a;color:#ddd;font-size:10px;padding:0 14px;display:flex;align-items:center;justify-content:space-between}
.header-icons{left:946px;top:26px;display:flex;gap:16px;align-items:center}
.badge{position:relative}
.badge sup{position:absolute;top:-6px;right:-7px;font-size:7px;color:var(--white)}
.main-nav{left:0;top:71px;width:1200px;height:66px;border-bottom:1px solid var(--line)}
.main-nav span{position:absolute;top:26px;font-size:11px;letter-spacing:1px;color:#444;white-space:nowrap}
.main-nav .active{font-weight:600;color:var(--ink);border-bottom:1px solid var(--ink);padding-bottom:2px}
.page-band{left:0;top:137px;width:1200px;height:76px;background:var(--band);border-bottom:1px solid #eee}
.page-title{left:161px;top:166px;font-size:14px;color:var(--ink)}
.crumbs{right:161px;top:169px;font-size:9px;color:var(--soft);display:flex;gap:8px}
.crumbs b{font-weight:400;color:var(--ink)}
.gallery{left:161px;top:289px;width:427px;height:464px;background:linear-gradient(180deg,#f3f3f3,#ececec)}
.thumb{top:765px;height:98px;background:var(--photo)}
.thumb.current{border:1px solid #bdbdbd}
.arrow-light{position:absolute;top:222px;color:#666;font-size:22px;font-weight:300}
.product-name{left:611px;top:284px;font-size:23px;font-weight:500}
.price{left:611px;top:320px;font-size:14px;font-weight:500}
.stars{right:160px;top:287px;font-size:12px;letter-spacing:1px}
.reviews{right:158px;top:307px;font-size:10px;color:var(--soft)}
.pid{right:159px;top:325px;font-size:9.5px}
.rule{height:1px;background:var(--line)}
.copy{left:611px;top:372px;width:430px;font-size:10.9px;font-weight:300;line-height:22.7px;color:#555}
.label{font-size:10.5px;color:var(--ink)}
.select{height:34px;border:1px solid #e2e2e2;font-size:10.5px;color:var(--muted);display:flex;align-items:center;padding:0 11px;justify-content:space-between}
.swatch{width:22px;height:20px;background:#aaaaaa}
.fit{left:897px;top:487px;font-size:8px;color:var(--muted);text-decoration:underline}
.qty{left:685px;top:575px;width:74px;height:45px;border:1px solid #e2e2e2;display:flex}
.qty .num{width:44px;display:flex;align-items:center;justify-content:center;font-size:12px}
.qty .steps{flex:1;border-left:1px solid #e2e2e2;display:flex;flex-direction:column}
.qty .steps i{flex:1;display:flex;align-items:center;justify-content:center;font-style:normal;font-size:8px}
.qty .steps i+i{border-top:1px solid #e2e2e2}
.wish{left:830px;top:590px;font-size:11px;display:flex;gap:6px;align-items:center}
.cart-btn{left:908px;top:574px;width:132px;height:46px;background:var(--dark);color:var(--white);font-size:11px;font-weight:600;display:flex;align-items:center;justify-content:center;border-radius:2px}
.meta-k{left:611px;font-size:10.5px}
.meta-v{left:685px;font-size:11px;color:var(--muted)}
.meta-v b{font-weight:400;color:var(--ink)}
.dot{display:inline-block;width:8px;height:8px;border-radius:50%;background:#9a9a9a;margin-right:9px}
.tabs-band{left:0;top:938px;width:1200px;height:307px;background:var(--band)}
.tab{top:990px;font-size:13px;color:var(--muted)}
.tab.on{color:var(--ink);font-weight:500}
.tab-text{left:156px;top:1054px;width:888px;text-align:center;font-size:11.2px;font-weight:300;line-height:27px;color:#333}
.tab-text u{text-underline-offset:2px}
.read-more{left:0;width:1188px;top:1160px;text-align:center;font-size:11px;font-weight:500}
.section-title{left:0;width:1200px;top:1312px;text-align:center;font-family:'Playfair Display',serif;font-weight:700;font-size:29px;color:var(--dark)}
.card-photo{top:1391px;width:202px;height:255px;background:linear-gradient(180deg,#f4f4f4,#ececec)}
.card-info{top:1662px;width:202px;text-align:center}
.card-info small{display:block;font-size:9px;letter-spacing:1.5px;color:var(--muted)}
.card-info h3{font-size:12px;font-weight:400;margin-top:2px}
.card-info hr{width:20px;border:0;border-top:1px solid #ccc;margin:10px auto 10px}
.card-info p{font-size:14px;font-weight:500}
.slide-btn{top:1500px;width:37px;height:37px;display:flex;align-items:center;justify-content:center}
.pager{left:572px;top:1762px;display:flex;gap:10px;align-items:center}
.pager i{width:10px;height:10px;border-radius:50%;background:#ddd;display:block}
.pager i.on{width:16px;height:16px;border:1px solid var(--ink);background:radial-gradient(circle,var(--ink) 4px,var(--white) 5px)}
.site-footer{left:0;top:1855px;width:1200px;height:317px;background:var(--band)}
.foot-logo{left:161px;top:1925px;color:var(--ink)}
.foot-h{top:1913px;font-size:13px;font-weight:500}
.foot-bar{top:1942px;width:22px;height:1px;background:#ccc}
.foot-list{font-size:10.5px;font-weight:300;color:#555;line-height:27px}
.foot-list b{font-weight:400;color:var(--ink)}
.news{left:835px;top:1962px;width:204px;height:26px;border-bottom:1px solid #888;font-size:10.5px;display:flex;justify-content:space-between;align-items:center}
.copyright{left:161px;top:2093px;font-size:11px;font-weight:300}
.copyright b{font-weight:500}
.pay{top:2093px;width:34px;height:21px;background:#1f1f1f;border-radius:2px}
</style>
</head>
<body>

<header class="abs site-header">
  <div class="abs logo" style="left:161px;top:32px">VELORA CASA</div>
  <div class="abs search">Search Any Product Here
    <svg width="11" height="11" viewBox="0 0 12 12"><circle cx="5" cy="5" r="4" fill="none" stroke="#ccc" stroke-width="1.2"/><path d="M8 8l3 3" stroke="#ccc" stroke-width="1.2"/></svg>
  </div>
  <div class="abs header-icons">
    <svg width="14" height="15" viewBox="0 0 14 15"><circle cx="7" cy="4" r="3.5" fill="#fff"/><path d="M0 15c0-5 3-7 7-7s7 2 7 7z" fill="#fff"/></svg>
    <span class="badge"><svg width="17" height="15" viewBox="0 0 17 15"><path d="M8.5 15L1.5 8A4 4 0 018.5 2.5 4 4 0 0115.5 8z" fill="#fff"/></svg><sup>2</sup></span>
    <span class="badge"><svg width="15" height="16" viewBox="0 0 15 16"><path d="M4.5 5V3.5a3 3 0 016 0V5" fill="none" stroke="#fff" stroke-width="1.3"/><path d="M1 5h13l-1 11H2z" fill="#fff"/></svg><sup>2</sup></span>
  </div>
</header>

<nav class="abs main-nav">
  <span style="left:341px">HOME</span>
  <span style="left:413px">ABOUT US</span>
  <span class="active" style="left:507px">WOMEN ⌄</span>
  <span style="left:602px">MEN ⌄</span>
  <span style="left:675px">CHILDREN ⌄</span>
  <span style="left:781px">CONTACT US</span>
</nav>

<section class="abs page-band"></section>
<h1 class="abs page-title" style="font-weight:400">FANCY LUXURY LINGERIES</h1>
<div class="abs crumbs">HOME <span>›</span> SHOP <span>›</span> WOMEN <span>›</span> LINGERIES <span>›</span> <b>LUXURY LINGERIES</b></div>

<div class="abs gallery" role="img" aria-label="Model wearing black mesh and vinyl halter lingerie set">
  <svg class="abs" style="left:378px;top:29px" width="20" height="20" viewBox="0 0 20 20" fill="none" stroke="#555" stroke-width="1.1"><path d="M1 6V1h5M1 1l6 6M19 6V1h-5M19 1l-6 6M1 14v5h5M1 19l6-6M19 14v5h-5M19 19l-6-6"/></svg>
  <span class="arrow-light" style="left:30px">‹</span>
  <span class="arrow-light" style="left:387px">›</span>
</div>
<div class="abs thumb" style="left:161px;width:99px" role="img" aria-label="Front view of lingerie set"></div>
<div class="abs thumb current" style="left:275px;width:92px" role="img" aria-label="Close front view of lingerie set"></div>
<div class="abs thumb" style="left:381px;width:99px" role="img" aria-label="Back view of lingerie set"></div>
<div class="abs thumb" style="left:489px;width:99px" role="img" aria-label="Lingerie set laid flat"></div>

<h2 class="abs product-name">Luxury Lingeries</h2>
<div class="abs price">$34.00</div>
<div class="abs stars">★★★★★</div>
<div class="abs reviews">(5 costumer reviews)</div>
<div class="abs pid">PRODUCT ID: 21399392</div>
<div class="abs rule" style="left:611px;top:356px;width:429px"></div>
<p class="abs copy">Artsy paleo aesthetic, vape utine letterpress pinboard bushwick twee. Artsy<br>man braid shabby chic kalvestrand pop-up cloud bread. Simply dummy text<br>is lorem ipsum amet postekamat.</p>
<div class="abs rule" style="left:611px;top:458px;width:429px"></div>

<div class="abs label" style="left:611px;top:486px">Pick Your Color</div>
<div class="abs label" style="left:835px;top:486px">Size</div>
<div class="abs fit">CLICK HERE TO FIND YOUR FIT SIZE</div>
<div class="abs select" style="left:611px;top:510px;width:202px">Grey <span style="display:flex;gap:12px;align-items:center">⌄<span class="swatch"></span></span></div>
<div class="abs select" style="left:835px;top:510px;width:203px">Choose An Option <span>⌄</span></div>

<div class="abs label" style="left:611px;top:590px;font-size:11.5px">Quantity:</div>
<div class="abs qty"><div class="num">1</div><div class="steps"><i>▲</i><i>▼</i></div></div>
<div class="abs wish"><svg width="12" height="11" viewBox="0 0 17 15"><path d="M8.5 14L1.5 7.5A4 4 0 018.5 2.5 4 4 0 0115.5 7.5z" fill="none" stroke="#222" stroke-width="1.5"/></svg>WISHLIST</div>
<div class="abs cart-btn">ADD TO CART</div>
<div class="abs rule" style="left:611px;top:651px;width:429px"></div>

<div class="abs meta-k" style="top:678px">Sku:</div><div class="abs meta-v" style="top:678px">1702</div>
<div class="abs meta-k" style="top:702px">Category:</div><div class="abs meta-v" style="top:702px">Underwear, <b>Stockings</b></div>
<div class="abs meta-k" style="top:729px">Tags:</div><div class="abs meta-v" style="top:729px">Women,&nbsp; Fashion</div>
<div class="abs meta-k" style="top:757px">Share:</div><div class="abs meta-v" style="top:760px"><i class="dot"></i><i class="dot"></i><i class="dot"></i><i class="dot"></i></div>

<section class="abs tabs-band"></section>
<div class="abs tab" style="left:383px">Description</div>
<div class="abs tab on" style="left:522px">Additional Information</div>
<div class="abs tab" style="left:737px">Reviews ( 5 )</div>
<div class="abs rule" style="left:161px;top:1023px;width:878px"></div>
<div class="abs" style="left:546px;top:1022px;width:109px;height:2px;background:var(--ink)"></div>
<p class="abs tab-text">Master cleanse sartorial me lyra kickmaker <u>hella fingerstache irony asymmetrical narwhal</u> adapt gaudrel. Koru edmond bulb brooklyn artsy iceland, locavore<br>organic 90's tumeric portlandesto normcore. Kalvestrand drinking vinegar taiyaki sustainabl semiotics banjo. Pok glossery la cruse pinboard humblebrageddo<br>twee. Edmond bulb prism +1 hot chicken pok pok bespoke blue flask salvia YOLO neutra.</p>
<div class="abs read-more">READ MORE<br><svg width="11" height="11" viewBox="0 0 11 11" fill="none" stroke="#222" stroke-width="1.3"><path d="M1 1l4.5 4 4.5-4M1 6l4.5 4 4.5-4"/></svg></div>

<h2 class="abs section-title">You May Also Like</h2>

<div class="abs card-photo" style="left:161px" role="img" aria-label="Model in black sheer baby doll"></div>
<div class="abs card-photo" style="left:386px" role="img" aria-label="Model in fishnet bodysuit"></div>
<div class="abs card-photo" style="left:611px" role="img" aria-label="Model in black bra and panties"></div>
<div class="abs card-photo" style="left:836px" role="img" aria-label="Model in black satin slip"></div>

<div class="abs card-info" style="left:161px"><small>LOREM IPSUM</small><h3>Luxury Lingerie Baby Doll</h3><hr><p>$23.00</p></div>
<div class="abs card-info" style="left:386px"><small>LOREM IPSUM</small><h3>Fishnet Luxury Lingeries</h3><hr><p>$39.00</p></div>
<div class="abs card-info" style="left:611px"><small>LOREM IPSUM</small><h3>Bra and Panties</h3><hr><p>$16.00</p></div>
<div class="abs card-info" style="left:836px"><small>LOREM IPSUM</small><h3>Sleeping Underwear Lingerie</h3><hr><p>$24.00</p></div>

<div class="abs slide-btn" style="left:143px;background:#e3e3e3"><svg width="16" height="10" viewBox="0 0 16 10" fill="none" stroke="#555" stroke-width="1.2"><path d="M15 5H1M5 1L1 5l4 4"/></svg></div>
<div class="abs slide-btn" style="left:1016px;background:var(--dark)"><svg width="16" height="10" viewBox="0 0 16 10" fill="none" stroke="#fff" stroke-width="1.2"><path d="M1 5h14M11 1l4 4-4 4"/></svg></div>
<div class="abs pager"><i></i><i class="on"></i><i></i></div>

<footer class="abs site-footer"></footer>
<div class="abs logo foot-logo">VELORA CASA</div>
<div class="abs foot-list" style="left:161px;top:1960px"><b>Phone Number:</b> 01/5830-217<br><b>E-Mail Address:</b> info@veloracasa.com<br><b>Working Hours:</b> Mon – Sat: 09 – 21 h</div>

<div class="abs foot-h" style="left:388px">Find Us At</div>
<div class="abs foot-bar" style="left:388px"></div>
<div class="abs foot-list" style="left:388px;top:1960px">Terms Of Use<br>Terms Of Purchase<br>Privacy Policy</div>

<div class="abs foot-h" style="left:612px">Information</div>
<div class="abs foot-bar" style="left:612px"></div>
<div class="abs foot-list" style="left:612px;top:1960px">Payment Methods<br>Delivery &amp; Shipping<br>Returns &amp; Refunds</div>

<div class="abs foot-h" style="left:835px">Newsletter</div>
<div class="abs foot-bar" style="left:835px"></div>
<div class="abs news">Your E-mail Address <svg width="11" height="10" viewBox="0 0 11 10" fill="none" stroke="#333" stroke-width="1"><path d="M1 5L10 1 7 9 5 6z"/></svg></div>
<div class="abs" style="left:835px;top:2015px;font-size:10.5px;display:flex;align-items:center;gap:2px">Find Us At: &nbsp;<i class="dot" style="background:#333"></i><i class="dot" style="background:#333"></i><i class="dot" style="background:#333"></i><i class="dot" style="background:#333"></i><i class="dot" style="background:#333"></i></div>

<div class="abs rule" style="left:161px;top:2070px;width:878px;background:#dedede"></div>
<div class="abs copyright"><b>Copyright © 2020 Velora Casa.</b> All Rights Reserved</div>
<div class="abs pay" style="left:921px"></div>
<div class="abs pay" style="left:963px"></div>
<div class="abs pay" style="left:1005px"></div>

</body>
</html>
```